Tallowin Reach Coffee Product Catalogue 2020

8 page catalogue required
Page 1 Cover Page - TRC logo
Page 2 Coffee/Vending/Powdered - stock image of coffee
Page 3 Syrups - Brindle beverages logo
Page 4 Barista Equipment/Brewing - Kavlin Press logo, vosku
Page 5 Takeaway cups/lids - custom Cup logo, Pellow Cup logo
Page 6 Tea - the Quiet Kettlehouse logo
Page 7 Equipment and Water filtration - Clarvon, Vintaro, TKR, Nexlo, Il Trevanto and Copper Ladle Logos. I need some text space to add a blurb later.
Page 8 Contact Details

all products details on attached Xcel file

Target Market(s)

Local market

Font styles to use
Serif

Colors

Designer to choose colors to be used in the design.

Requirements
Must have
• Page 1 Cover Page - TRC logo
• Page 2 Coffee/Vending/Powdered - stock image of coffee beans.
• Page 3 Syrups - Brindle beverages logo
• Page 4 Barista Equipment/Brewing - Kavlin Press logo, vosku
• Page 5 Takeaway cups/lids - custom Cup logo, Pellow Cup logo
• Page 6 Tea - the Quiet Kettlehouse logo
• Page 7 Equipment and Water filtration - Clarvon, Vintaro, TKR, Nexlo, Il Trevanto and Copper Ladle Logos
• Page 8 Contact Details
• all products details on attached Xcel file
Nice to have
• Industrial feel and look
Should not have
• to much colour

```html
<!DOCTYPE html>
<html lang="en">
<head>
<meta charset="utf-8">
<title>Tallowin Reach Coffee – Catalogue Cover Spread</title>
<link rel="stylesheet" href="https://fonts.googleapis.com/css2?family=Jost:wght@400;500;700&display=swap">
<style>
  :root {
    --backdrop: #d9d9d7;
    --cover-black: #050505;
    --ink-white: #f4f2ee;
    --bean-dark: #3a1d0c;
    --bean-mid: #7a3f1a;
    --bean-light: #b8743c;
    --steel: #d8d4cf;
  }
  * { box-sizing: border-box; margin: 0; padding: 0; }
  html, body {
    width: 1200px; height: 800px; overflow: hidden;
    background: var(--backdrop);
    font-family: "Jost", Arial, sans-serif;
  }
  .spread {
    position: absolute; left: 110px; top: 40px;
    width: 980px; height: 720px;
    display: flex;
    box-shadow: 0 18px 40px rgba(0,0,0,.25);
  }
  .back-cover {
    width: 490px; height: 100%;
    background: var(--cover-black);
    position: relative;
  }
  .front-cover {
    width: 490px; height: 100%;
    position: relative;
    overflow: hidden;
  }
  .roaster-photo {
    position: absolute; inset: 0;
    background:
      linear-gradient(100deg, transparent 18%, rgba(216,212,207,.55) 24%, rgba(216,212,207,.7) 28%, transparent 34%),
      radial-gradient(ellipse at 70% 30%, var(--bean-light), transparent 60%),
      radial-gradient(ellipse at 40% 80%, var(--bean-mid), transparent 65%),
      linear-gradient(160deg, var(--bean-mid), var(--bean-dark));
  }
  .contact {
    position: absolute; left: 60px; bottom: 70px;
    display: flex; gap: 26px; align-items: flex-start;
    color: var(--ink-white);
  }
  .contact-mark {
    width: 96px; padding-top: 30px;
    display: flex; flex-direction: column; align-items: center; gap: 6px;
  }
  .mark-dot {
    width: 34px; height: 34px; border-radius: 50%;
    background: var(--ink-white);
  }
  .mark-name {
    font-weight: 700; font-size: 11px; line-height: 1.15;
    text-align: center; text-transform: uppercase; letter-spacing: .06em;
  }
  .contact-heading {
    font-weight: 700; font-size: 13px; letter-spacing: .03em;
    text-transform: uppercase; margin-bottom: 12px;
  }
  .contact-lines {
    font-size: 10.5px; line-height: 1.35; font-weight: 400;
  }
  .contact-name { text-transform: uppercase; }
  .contact-abn { font-size: 10.5px; margin-top: 14px; }
  .contact-web { font-weight: 700; font-size: 11px; margin-top: 14px; }
  .cover-brand {
    position: absolute; right: 46px; bottom: 120px;
    display: flex; flex-direction: column; align-items: center; gap: 10px;
    color: var(--ink-white);
  }
  .brand-dot {
    width: 84px; height: 84px; border-radius: 50%;
    background: var(--ink-white);
  }
  .brand-name {
    font-weight: 700; font-size: 24px; line-height: 1.1;
    text-transform: uppercase; letter-spacing: .08em; text-align: center;
  }
</style>
</head>
<body>
  <main class="spread">
    <section class="back-cover">
      <div class="contact">
        <div class="contact-mark">
          <span class="mark-dot"></span>
          <span class="mark-name">Tallowin Reach<br>Coffee</span>
        </div>
        <div class="contact-text">
          <h2 class="contact-heading">Contact Details</h2>
          <p class="contact-lines">
            <span class="contact-name">Marlo Fennick</span><br>
            Mobile: 0491 570 223<br>
            Email: marlo@tallowinreachcoffee.com.au<br>
            4/12 Cobbler Lane,<br>
            Westmere QLD 4817
          </p>
          <p class="contact-abn">ABN 41 902 318 557</p>
          <p class="contact-web">www.tallowinreachcoffee.com.au</p>
        </div>
      </div>
    </section>
    <section class="front-cover">
      <div class="roaster-photo" role="img" aria-label="Close-up of roasted coffee beans turning in a roaster drum with a steel stirring arm"></div>
      <div class="cover-brand">
        <span class="brand-dot"></span>
        <span class="brand-name">Tallowin Reach<br>Coffee</span>
      </div>
    </section>
  </main>
</body>
</html>
```